Cool business cards

Use my existing logo from tallow brook (see images I have uploaded) and design a really cool non-stuffy business card. I am a divorce mediator.

```html
<!DOCTYPE html>
<html lang="en">
<head>
<meta charset="utf-8">
<title>Tallow Brook – Business Card</title>
<link rel="stylesheet" href="https://fonts.googleapis.com/css2?family=Roboto:wght@300;400&family=Khand:wght@600&display=swap">
<style>
  :root {
    --backdrop: #b9b9b9;
    --teal: #3a9fa4;
    --green: #3b8763;
    --paper: #f4f4f2;
    --ink: #2a2a2a;
    --white: #ffffff;
  }
  * { margin: 0; padding: 0; box-sizing: border-box; }
  html, body { width: 1200px; height: 576px; overflow: hidden; }
  body {
    background: var(--backdrop);
    position: relative;
    font-family: "Roboto", Arial, sans-serif;
  }
  .card {
    position: absolute;
    top: 139px;
    width: 485px;
    height: 293px;
    border-radius: 12px;
    overflow: hidden;
  }
  .card--front {
    left: 82px;
    background: linear-gradient(120deg, var(--teal) 0%, #3c9488 45%, var(--green) 100%);
  }
  .card--back {
    left: 602px;
    background: var(--paper);
  }
  .brand { position: absolute; text-align: center; }
  .brand__name {
    font-family: "Roboto", Arial, sans-serif;
    font-weight: 300;
    letter-spacing: 1px;
    line-height: 1;
  }
  .brand__tagline {
    display: flex;
    align-items: center;
    gap: 8px;
    font-weight: 400;
    white-space: nowrap;
  }
  .brand__rule { flex: 1; height: 2px; }
  .card--front .brand { left: 0; right: 0; top: 100px; }
  .card--front .brand__name { color: var(--white); font-size: 40px; }
  .card--front .brand__tagline {
    width: 300px; margin: 14px auto 0;
    color: var(--white); font-size: 14px;
  }
  .card--front .brand__rule { background: var(--white); }
  .card--back .brand { left: 29px; top: 46px; width: 218px; }
  .card--back .brand__name { color: var(--green); font-size: 29px; text-align: left; }
  .card--back .brand__tagline {
    margin-top: 10px; color: var(--teal); font-size: 10.5px;
  }
  .card--back .brand__rule { background: var(--green); }
  .person { position: absolute; left: 28px; top: 161px; color: var(--ink); }
  .person__name {
    font-family: "Khand", "Arial Narrow", sans-serif;
    font-weight: 600; font-size: 21px; color: var(--green); line-height: 1;
  }
  .person__role { font-size: 13px; margin-top: 5px; }
  .person__address { font-size: 13px; line-height: 18px; margin-top: 26px; }
  .contact {
    position: absolute; left: 256px; top: 177px;
    list-style: none; font-size: 13px; color: var(--ink);
  }
  .contact li { display: flex; align-items: center; height: 18.5px; }
  .contact svg { width: 11px; height: 11px; margin-right: 11px; fill: var(--green); }
  .band-strip {
    position: absolute; left: 0; bottom: 0; width: 215px; height: 11px;
    background: var(--teal);
  }
  .band { position: absolute; left: 0; bottom: 0; width: 485px; height: 39px; }
  .band__services {
    position: absolute; left: 222px; bottom: 11px;
    font-size: 11.5px; color: var(--white); white-space: nowrap; word-spacing: 1px;
  }
</style>
</head>
<body>
  <section class="card card--front">
    <div class="brand">
      <div class="brand__name">Tallow Brook</div>
      <div class="brand__tagline"><span class="brand__rule"></span>I AM A DIVORCE MEDIATOR<span class="brand__rule"></span></div>
    </div>
  </section>

  <section class="card card--back">
    <div class="brand">
      <div class="brand__name">Tallow Brook</div>
      <div class="brand__tagline"><span class="brand__rule"></span>I AM A DIVORCE MEDIATOR<span class="brand__rule"></span></div>
    </div>

    <div class="person">
      <div class="person__name">Maren Ellis Hart</div>
      <div class="person__role">Managing Director</div>
      <div class="person__address">87 Willow Lane, Ashford,<br>Brookvale, US 204815</div>
    </div>

    <ul class="contact">
      <li><svg viewBox="0 0 12 12"><path d="M1 4c0-1.5 2-2.5 5-2.5S11 2.5 11 4v1H8.5V4h-5v1H1zM3 6h6l1.5 4.5h-9z"/></svg>555-014-2290</li>
      <li><svg viewBox="0 0 12 12"><path d="M0.5 2.5h11v7h-11z M1.5 3.5 6 7l4.5-3.5" stroke="#f4f4f2" stroke-width="0.9"/></svg>maren@tallowbrook.com</li>
      <li><svg viewBox="0 0 12 12"><circle cx="6" cy="6" r="5.3"/><path d="M0.7 6h10.6M6 0.7v10.6M2 3.3h8M2 8.7h8" stroke="#f4f4f2" stroke-width="0.7" fill="none"/></svg>www.tallowbrook.com</li>
    </ul>

    <div class="band-strip"></div>
    <svg class="band" viewBox="0 0 485 39" aria-hidden="true">
      <path d="M194 39 L210 6 Q213 0 220 0 H485 V39 Z" fill="var(--green)"/>
    </svg>
    <div class="band__services">Consulting&nbsp; | &nbsp;Healthcare IT&nbsp; | &nbsp;Transformation</div>
  </section>
</body>
</html>
```